Regional Showdown Flyer for Holiday Program

Need a one page flyer, can be back to front or one page, ensuring you can fit all information, colourful, aimed at a market of 8-13 year old boys and girls.
The flyer needs to be noticed, needs to have certain information on it and needs to be Autralian Rule Football orientated.
Have uploaded file so you can understand the style (not content), style of flyer I am looking at getting submitted.

Target Market(s)

8-13 year old boys and girls and their parents.

Requirements
Must have
• Regional Showdown Event
• Price for Regional Showdown Day will be $85
• Strictly Limited Places, only the best footballers should enter this challenge
• Inaugural event, be the first Regional Showdown Winner for your age!
• Do you love a challenge! Put yourself to the test!
• Are you up to it - Water Slide Goal Kicking Contest! The fastest kick in the West (tested by our very own speed gun)! Can you survive the Footy Titan Trail or Last One Standing Goal Kicking! These challenges are crazy are super fun!
• If you think you can deliver on the big stage then this is for YOU!
• All District age winners will receive prizes, awards and the adulation from all their peers!
• Year's 3-5 from 9am to 12pm
• Year's 6-8 from 1-4pm
• All challengers compete against their own age
• Lunch Provided
• Monday 16th April - Upper Tarrowby Regional Showdown Day at Tarrowby Oval
• Tuesday 17th April - North Tarrowby Regional Showdown Day at Kilmorna Reserve
• Wednesday 18th April - Yarlo Regional Showdown Day - Dunhaven Football Club
• Every Challenge Participant receives a District Football!
• Need to put all 3 District Football Logos on the bottom of the flyer, logos attached at bottom.
Nice to have
• Plenty of colour, if you can fit all information on one page that would be fine
Should not have
• Dull, boring, any footballs should be Aussie Rules footballs not NFL or soccer

```html
<!DOCTYPE html>
<html lang="en">
<head>
<meta charset="utf-8">
<title>Regional Showdown Event Flyer</title>
<link href="https://fonts.googleapis.com/css2?family=Lilita+One&family=Londrina+Solid:wght@400;900&display=swap" rel="stylesheet">
<style>
  :root{
    --page:#e9e4dc;
    --field:#236b3c;
    --line:#ffffff;
    --title-red:#e8335a;
    --pink:#f23fa6;
    --hot-pink:#e8308f;
    --yellow:#ece552;
    --mint:#5fd3a8;
    --sky:#17a2d6;
    --ball:#a3431f;
    --ink:#111111;
    --band:#0db657;
    --gold:#f4d84a;
    --brand-blue:#1f4fa0;
    --brand-green:#168c6a;
    --brand-red:#d81d2a;
  }
  html,body{margin:0;padding:0;width:1200px;height:1200px;overflow:hidden;background:var(--page);}
  p{margin:0;}
  .flyer{position:absolute;left:176px;top:0;width:848px;height:1200px;background:#fff;overflow:hidden;font-family:"Londrina Solid",sans-serif;}
  .field{position:absolute;inset:0;}
  .ball{position:absolute;left:160px;top:170px;width:500px;height:260px;border-radius:50%;background:radial-gradient(ellipse at 50% 40%,#c2592b,var(--ball) 70%);transform:rotate(-18deg);}
  .title{position:absolute;left:0;top:0;width:848px;height:280px;}
  .title text{font-family:"Lilita One",sans-serif;fill:var(--title-red);stroke:#fff;stroke-width:10px;paint-order:stroke;stroke-linejoin:round;}
  .tag{position:absolute;color:var(--ink);text-align:center;line-height:1.15;font-family:"Londrina Solid",sans-serif;}
  .tag--challenge{left:32px;top:266px;width:268px;height:100px;background:var(--pink);transform:rotate(3deg);font-size:23px;display:flex;align-items:center;justify-content:center;}
  .tag--trail{left:40px;top:410px;width:292px;height:94px;background:var(--yellow);transform:rotate(-1deg);font-size:23px;display:flex;align-items:center;justify-content:center;}
  .tag--kick{left:8px;top:565px;width:270px;height:100px;background:var(--pink);transform:rotate(-3deg);color:var(--yellow);font-size:23px;display:flex;flex-direction:column;align-items:center;justify-content:center;}
  .tag--kick small{font-size:16px;}
  .tag--slide{left:36px;top:676px;width:318px;height:96px;background:var(--mint);transform:rotate(-4deg);font-size:30px;display:flex;align-items:center;justify-content:center;}
  .gift{position:absolute;left:240px;top:268px;width:380px;text-align:center;color:#fff;font-size:22px;line-height:1.25;text-shadow:0 2px 3px rgba(0,0,0,.6);}
  .price{position:absolute;z-index:5;left:666px;top:222px;width:132px;height:132px;border-radius:50%;background:#fff;border:5px solid var(--gold);box-sizing:border-box;text-align:center;color:var(--title-red);}
  .price b{display:block;font-family:"Lilita One",sans-serif;font-size:52px;line-height:1;margin-top:20px;font-weight:400;}
  .price span{font-size:16px;}
  .photo{position:absolute;border-radius:50%;border:8px solid var(--sky);box-sizing:border-box;}
  .photo--team{left:292px;top:374px;width:296px;height:296px;background:linear-gradient(160deg,#7ea34a,#3f5f2a 60%,#24325e);}
  .photo--squad{left:553px;top:290px;width:178px;height:178px;background:linear-gradient(160deg,#f3efe6,#c8322a 65%);}
  .photo--player{left:603px;top:450px;width:178px;height:178px;background:linear-gradient(160deg,#b8d1a1,#d9b39a 55%,#202028);}
  .photo--helmets{left:520px;top:606px;width:212px;height:212px;background:linear-gradient(160deg,#8eb46a,#8c2030 60%,#e8e8e8);}
  .ask{position:absolute;left:36px;top:788px;font-size:32px;color:var(--ink);}
  .facts{position:absolute;top:846px;font-size:29px;line-height:34px;color:var(--hot-pink);text-transform:uppercase;white-space:nowrap;}
  .facts--left{left:36px;}
  .facts--right{left:463px;}
  .stage{position:absolute;left:0;top:924px;width:848px;text-align:center;font-size:29px;color:var(--ink);white-space:nowrap;}
  .details{position:absolute;left:23px;top:966px;width:800px;height:56px;border-radius:12px;background:var(--band);text-align:center;font-size:17px;line-height:23px;color:var(--ink);padding-top:5px;box-sizing:border-box;}
  .dates{position:absolute;left:0;top:1030px;width:848px;text-align:center;font-size:17px;line-height:21px;color:var(--ink);}
  .dates b{color:var(--hot-pink);font-weight:400;}
  .partners{position:absolute;left:0;top:1100px;width:848px;height:80px;display:flex;justify-content:space-around;align-items:center;}
  .partner{display:flex;align-items:center;gap:10px;font-weight:900;font-size:28px;}
  .partner i{display:block;width:22px;height:22px;border-radius:50%;}
  .partner--stingrays{color:var(--brand-blue);} .partner--stingrays i{background:var(--brand-blue);}
  .partner--yarlo{color:var(--brand-green);} .partner--yarlo i{background:var(--brand-green);}
  .partner--kelpies{color:var(--brand-red);} .partner--kelpies i{background:var(--brand-red);}
</style>
</head>
<body>
<main class="flyer">
  <svg class="field" width="848" height="1200" viewBox="0 0 848 1200">
    <defs>
      <pattern id="hash" width="18" height="32" patternUnits="userSpaceOnUse">
        <rect width="18" height="14" fill="#fff"/>
      </pattern>
    </defs>
    <rect width="848" height="900" fill="var(--field)"/>
    <rect y="20" width="848" height="10" fill="#fff"/>
    <rect y="42" width="848" height="10" fill="#fff"/>
    <rect y="208" width="848" height="10" fill="#fff"/>
    <rect y="393" width="848" height="10" fill="#fff"/>
    <rect y="56" width="18" height="330" fill="url(#hash)"/>
    <rect y="408" width="18" height="350" fill="url(#hash)"/>
    <rect x="830" y="56" width="18" height="330" fill="url(#hash)"/>
    <rect x="830" y="408" width="18" height="350" fill="url(#hash)"/>
    <polygon points="748,718 790,718 769,676" fill="#fff"/>
    <polygon points="52,86 92,86 72,120" fill="#fff"/>
    <path d="M0 750 C200 720 420 780 600 820 C700 840 790 830 848 812 L848 850 C760 870 660 866 560 850 C400 820 200 760 0 780 Z" fill="var(--sky)"/>
    <path d="M0 780 C200 760 400 820 560 850 C660 866 760 870 848 850 L848 1200 L0 1200 Z" fill="#fff"/>
  </svg>

  <div class="ball" role="img" aria-label="Aussie Rules football behind the heading"></div>

  <svg class="title" viewBox="0 0 848 280">
    <path id="arc" d="M40 180 Q420 10 810 150" fill="none"/>
    <text font-size="76"><textPath href="#arc" startOffset="50%" text-anchor="middle">Regional Showdown</textPath></text>
    <text x="432" y="250" font-size="84" text-anchor="middle">Event</text>
  </svg>

  <p class="tag tag--challenge">Do you love a challenge !<br>Put yourself to the test !</p>
  <p class="gift">Every Challenge Participant receives a<br>District Football !</p>
  <p class="tag tag--trail">Can you survive the<br>Footy Titan Trail</p>
  <p class="tag tag--kick">The fastest kick in the West<small>(tested by our very own speed gun) !</small></p>
  <p class="tag tag--slide">Water Slide Goal<br>Kicking Contest !</p>

  <div class="photo photo--team" role="img" aria-label="Photo of two young players in jerseys on the grass"></div>
  <div class="photo photo--squad" role="img" aria-label="Photo of a junior squad in red holding a football"></div>
  <div class="photo photo--player" role="img" aria-label="Photo of a girl holding a football on the oval"></div>
  <div class="photo photo--helmets" role="img" aria-label="Photo of young players in a huddle"></div>
  <div class="price"><b>$85</b><span>PRICE FOR DAY</span></div>

  <p class="ask">ARE YOU UP TO IT</p>
  <p class="facts facts--left">Strictly limited places<br>Lunch provided</p>
  <p class="facts facts--right">Inaugural event<br>Last One Standing goal kicking!</p>
  <p class="stage">If you think you can deliver on the big stage then this is for YOU !</p>
  <div class="details">All District age winners will receive prizes, awards and the adulation from all their peers !<br>Year's 3-5 from 9am to 12pm - Year's 6-8 from 1-4pm - All challengers compete against their own age</div>
  <p class="dates"><b>Monday 16th April</b> - Upper Tarrowby Regional Showdown Day at Tarrowby Oval<br><b>Tuesday 17th April</b> - North Tarrowby Regional Showdown Day at Kilmorna Reserve<br><b>Wednesday 18th April</b> - Yarlo Regional Showdown Day - Dunhaven Football Club</p>

  <div class="partners">
    <div class="partner partner--stingrays"><i></i>Stingrays District</div>
    <div class="partner partner--yarlo"><i></i>Yarlo District</div>
    <div class="partner partner--kelpies"><i></i>Kelpies District</div>
  </div>
</main>
</body>
</html>
```